Clinical Hypnotherapist needs business card design

I need a business card design that gives the impression of being approachable yet professional. As a clinical hypnotherapist I need to create trust from my clients to allow me access to their inner mind to enable them to make changes and to start to live the life that they want to live. My website is www.serenvale.com.au and I would like my business cards to reflect my website. I would like a space for appointment details on the back of the card.

```html
<!DOCTYPE html>
<html lang="en">
<head>
<meta charset="utf-8">
<title>Clara Dunmore – Business Card</title>
<link rel="stylesheet" href="https://fonts.googleapis.com/css2?family=Lora:ital,wght@0,400;0,600;1,500&display=swap">
<style>
  :root {
    --page-bg: #d9d7dc;
    --purple-deep: #1e0b2e;
    --purple-mid: #3b1560;
    --purple-bright: #4c1c7a;
    --photo-violet: #7a5fb8;
    --photo-blue: #4a4fb0;
    --ink-light: #f3eefa;
    --ink-soft: #d8cce6;
    --ink-dark: #2a1446;
    --panel-white: #ffffff;
    --rule: #3a2460;
  }
  * { box-sizing: border-box; margin: 0; padding: 0; }
  html, body {
    width: 1200px; height: 1000px; overflow: hidden;
    background: var(--page-bg);
    font-family: "Lora", Georgia, serif;
  }
  .canvas {
    position: relative; width: 1200px; height: 1000px;
    display: flex; align-items: center; justify-content: center; gap: 50px;
  }
  .card {
    position: relative; width: 540px; height: 310px; overflow: hidden;
    border-radius: 4px;
    box-shadow: 0 10px 28px rgba(30, 10, 50, 0.25);
  }

  /* Front */
  .card--front {
    background: radial-gradient(ellipse at 70% 30%, var(--purple-bright) 0%, var(--purple-mid) 45%, var(--purple-deep) 100%);
    color: var(--ink-light);
  }
  .front__identity {
    position: absolute; left: 0; right: 0; top: 34px; text-align: center;
  }
  .front__name {
    font-style: italic; font-weight: 500; font-size: 38px; letter-spacing: 0.5px;
  }
  .front__title { font-size: 17px; color: var(--ink-soft); margin-top: 2px; }
  .front__contact {
    position: absolute; left: 0; right: 0; top: 118px; text-align: center;
    font-size: 17px; line-height: 26px; color: var(--ink-light);
  }
  .front__contact .divider {
    width: 150px; height: 1px; margin: 4px auto 6px;
    background: rgba(243, 238, 250, 0.35);
  }
  .front__photo {
    position: absolute; left: 0; right: 0; top: 196px; height: 56px;
    background: linear-gradient(180deg, var(--photo-violet), var(--photo-blue));
  }
  .front__web {
    position: absolute; left: 0; right: 0; bottom: 14px; text-align: center;
    font-size: 19px; color: var(--ink-light);
  }

  /* Back */
  .card--back { background: var(--panel-white); color: var(--ink-dark); }
  .back__band {
    position: absolute; left: 0; right: 0;
    background: linear-gradient(90deg, var(--purple-deep), var(--purple-mid) 60%, var(--purple-deep));
    color: var(--ink-light);
  }
  .back__band--top { top: 0; height: 62px; text-align: right; padding: 8px 26px 0 0; }
  .back__name { font-style: italic; font-weight: 500; font-size: 24px; line-height: 28px; }
  .back__title { font-size: 13px; color: var(--ink-soft); margin-right: 14px; }
  .back__band--bottom {
    bottom: 0; height: 54px; text-align: center;
    font-size: 11.5px; letter-spacing: 1px; line-height: 17px; padding-top: 10px;
  }
  .appointment {
    position: absolute; left: 0; right: 0; top: 62px; bottom: 54px;
    padding: 18px 30px 0;
  }
  .appointment__heading { text-align: center; font-weight: 600; font-size: 17px; }
  .appointment__days {
    display: flex; justify-content: space-between; margin: 20px 12px 0;
    font-weight: 600; font-size: 15px; letter-spacing: 0.5px;
  }
  .appointment__slots {
    display: flex; align-items: flex-end; gap: 10px; margin-top: 46px;
    font-weight: 600; font-size: 14px;
  }
  .slot-line { flex: 1; height: 1px; background: var(--rule); margin-bottom: 4px; }
  .slot-line--short { flex: 0.8; }
  .ampm { margin-left: 8px; }
</style>
</head>
<body>
<main class="canvas">

  <section class="card card--front" aria-label="Business card front">
    <div class="front__identity">
      <h1 class="front__name">Clara Dunmore</h1>
      <p class="front__title">clinical hypnotherapist</p>
    </div>
    <div class="front__contact">
      <div class="divider"></div>
      <p>0400 512 368</p>
      <p>clara@serenvale.com.au</p>
    </div>
    <div class="front__photo" role="img" aria-label="Photograph of a sunset over a calm ocean horizon"></div>
    <p class="front__web">www.serenvale.com.au</p>
  </section>

  <section class="card card--back" aria-label="Business card back">
    <header class="back__band back__band--top">
      <p class="back__name">Clara Dunmore</p>
      <p class="back__title">clinical hypnotherapist</p>
    </header>
    <div class="appointment">
      <p class="appointment__heading">Your appointment</p>
      <div class="appointment__days">
        <span>MON</span><span>TUE</span><span>WED</span><span>THU</span><span>FRI</span>
      </div>
      <div class="appointment__slots">
        <span>DATE:</span><span class="slot-line"></span>
        <span>TIME:</span><span class="slot-line slot-line--short"></span>
        <span class="ampm">AM&nbsp;&nbsp;PM</span>
      </div>
    </div>
    <footer class="back__band back__band--bottom">
      <p>IF YOU ARE UNABLE TO KEEP APPOINTMENT</p>
      <p>PLEASE CALL 0400 512 368</p>
    </footer>
  </section>

</main>
</body>
</html>
```